London Based Property Finding Company - have logo already

We find property for private purchasers and investors in London, UK.  We work for the BUYER, whereas estate agencies/real estate companies work for the seller. We offer a much more personalised service to UK and overseas purchasers.

We would like the following:

*A double sided business card

*A letterhead

We have attached two versions of the logo. Each logo style is set on two different coloured backgrounds. Please choose one of the two designs, whichever you prefer or feel more comfortable with, and produce one in black and one in white background.

This applies to both pieces of stationery.

THE BUSINESS CARD:

We would like the company name placed on its own on one side of the card and the contact details and what we do on the other.

e.g.

SIDE 1:

BRAMWELL PROPERTY FINDERS

SIDE 2:

Owen Bramwell

t: 0208 394 2261

m: +44(0)7940 318 472

e: info@bramwellpropertyfinders.co.uk

w: bramwellpropertyfinders.co.uk

London Property Finders and Search Agents

I will leave the layout up to you, but a minimalist layout is preferred. If you would like to put additional detial or design on the card then that is up to, but not specified.

It is optional to have the company name on side 2, but if you do use it, please make it smaller. than on the 1st side.

The design needs to be simple, professional and not too in your face.

If you are using the black background design on side 1 for the logo, then maybe a white backgounnd can be used on side 2 with a black typeface.

The type face for the contacts details should be sans serif standard typeface. Please experiment with the desciprtion.

-

THE LETTERHEAD;

You can experiment with the layout for the letterhead. e.g logo centre aligned on the top of the page with the contact details and address at the bottom of the page OR the logo, description running along a bar on the top of the page with the contact details and website address at the bottom. Please try and experiment with this, but the less 'busy', the better.

Here is info that needs to be on the letterhead.

Bramwell Property Finders

t: 0208 394 2261

m: +44(0)7940 318 472

(PLEASE NOTE; the below company info must be placed at the bottom of the page as a footer, in small text.)

Pemberly Holdings Ltd Trading as Bramwell Property Finders, a company registered in England & Wales, No.5917302 , Registered office is 41 Kelmscott House, Ashdown Lane, London, SW9 7QJ, t: 0208 394 2261, m: +44(0)7940 318 472, e: info@bramwellpropertyfinders.co.uk

Best of luck!

Thank you

Dear Designer,

I have now attached the supporting files to this brief.

Thanks,

Owen Bramwell
Bramwell Property Finders

```html
<!DOCTYPE html>
<html lang="en">
<head>
<meta charset="utf-8">
<title>Bramwell Property Finders – Letterhead</title>
<link href="https://fonts.googleapis.com/css2?family=Source+Sans+3:wght@400;600&display=swap" rel="stylesheet">
<style>
  :root {
    --paper: #ffffff;
    --navy: #1b2a78;
    --maroon: #5a1a20;
    --rule: #4a1117;
  }
  html, body {
    margin: 0;
    padding: 0;
    width: 1200px;
    height: 1200px;
    overflow: hidden;
    background: var(--paper);
  }
  .letterhead {
    position: relative;
    width: 1200px;
    height: 1200px;
    background: var(--paper);
    font-family: "Source Sans 3", "Myriad Pro", Arial, sans-serif;
  }
  .margin-rule {
    position: absolute;
    left: 68px;
    top: 115px;
    width: 5px;
    height: 1078px;
    background: var(--rule);
  }
  .brand-name {
    position: absolute;
    right: 50px;
    top: 44px;
    margin: 0;
    font-size: 34px;
    font-weight: 600;
    letter-spacing: 0.04em;
    color: var(--navy);
    line-height: 1;
    white-space: nowrap;
  }
  .contact-block {
    position: absolute;
    right: 56px;
    top: 124px;
    margin: 0;
    font-style: normal;
    text-align: right;
    color: var(--maroon);
    font-size: 16px;
    line-height: 20px;
  }
  .contact-block span { display: block; }
  .company-footer {
    position: absolute;
    left: 0;
    right: 0;
    top: 1150px;
    text-align: center;
    color: var(--navy);
    font-size: 11px;
    line-height: 14.5px;
  }
  .company-footer p { margin: 0; }
</style>
</head>
<body>
<main class="letterhead">
  <div class="margin-rule"></div>

  <header>
    <h1 class="brand-name">BRAMWELL PROPERTY FINDERS</h1>
    <address class="contact-block">
      <span>t: 0208 394 2261</span>
      <span>m: +44(0)7940 318 472</span>
      <span>e: info@bramwellpropertyfinders.co.uk</span>
      <span>w: bramwellpropertyfinders.co.uk</span>
    </address>
  </header>

  <footer class="company-footer">
    <p>Pemberly Holdings Ltd Trading as Bramwell Property Finders, a company registered in England &amp; Wales, No.5917302</p>
    <p>Registered office is 41 Kelmscott House, Ashdown Lane, London, SW9 7QJ</p>
    <p>t: 0208 394 2261, m: +44(0)7940 318 472, e: info@bramwellpropertyfinders.co.uk</p>
  </footer>
</main>
</body>
</html>
```